Business Card Design Project

I am looking for a minimal matte background/shiny (spot UV) ink monochromatic design with a splash of neon color.

the card should be 2 sided, logo only on one side - all info and possibly logo on the other.

My creative director described the colors he imagined for the design to be:
'it's a dark field, like charcoal or a really dark burgundy, or deep blue, shot through with a neon—but just a tiny bit of it. so a charcoal field with a laser-thin streak of electric lime, safety orange, or cobalt blue. really beautiful stuff.'

here are some samples of the types of cards I am trying to create:
http://www.pictavault.example/photos/dawnpress/6967376935/in/photostream -> Vandrelle Lustre

http://www.pictavault.example/photos/dawnpress/6497659409/in/photostream -> Standard Coated (14pt/matte) with SPOT UV

http://www.pictavault.example/photos/dawnpress/6497658995/in/photostream/ -> Heavy Corvane with Raised Ink

http://www.pictavault.example/photos/dawnpress/6275629165/in/photostream/ -> Standard Coated (14pt/matte) with SPOT UV

Here is my logo:
https://www.filecrate.example/s/sigym192mlh58ge/quillorb%20logotype%20final.ai

Here are the details for info:
Dorian Elwood Marsh
email - dorian@quillorb.example
mobile - 555 013 2867
web -
quillorb.example: inventive technology applications
quillorb-tv.example: innovative video advertising

please let me know if there is anything at all that you need.

Target Market(s)

mid to large agencies that require interactive design and entrepreneurial/startup individuals/companies that need application development.

Industry/Entity Type

Safety

Requirements
Must have
• logo only on one side

```html
<!DOCTYPE html>
<html lang="en">
<head>
<meta charset="utf-8">
<title>Quillorb Business Card</title>
<link rel="stylesheet" href="https://fonts.googleapis.com/css2?family=Bebas+Neue&display=swap">
<style>
  :root {
    --page-bg: #e4e2df;
    --card-dark: #0c0c0e;
    --card-mid: #1c1c20;
    --ink-white: #f4f6ff;
    --neon-cobalt: #3b4dff;
    --card-shadow: rgba(0, 0, 0, 0.35);
  }
  * { box-sizing: border-box; margin: 0; padding: 0; }
  html, body {
    width: 1164px;
    height: 1200px;
    overflow: hidden;
    background: var(--page-bg);
    font-family: "Bebas Neue", "Arial Narrow", sans-serif;
  }
  .canvas {
    position: relative;
    width: 1164px;
    height: 1200px;
  }
  .card {
    position: absolute;
    top: 215px;
    width: 440px;
    height: 770px;
    overflow: hidden;
    box-shadow: 0 14px 40px var(--card-shadow);
  }
  .card--front { left: 100px; }
  .card--back { left: 624px; }
  .card__texture {
    position: absolute;
    inset: 0;
    background:
      radial-gradient(ellipse at 50% 45%, var(--card-mid) 0%, var(--card-dark) 75%);
  }
  .brand {
    position: absolute;
    writing-mode: vertical-rl;
    color: var(--ink-white);
    line-height: 1;
    white-space: nowrap;
  }
  .brand--front {
    top: 60px;
    left: 50%;
    transform: translateX(-50%);
    font-size: 110px;
    letter-spacing: 0.12em;
  }
  .brand--back {
    top: 435px;
    left: 323px;
    font-size: 34px;
    letter-spacing: 0.12em;
  }
  .brand-dot {
    position: absolute;
    border-radius: 50%;
    background: var(--neon-cobalt);
  }
  .brand-dot--front {
    width: 26px;
    height: 26px;
    left: 207px;
    top: 640px;
  }
  .brand-dot--back {
    width: 12px;
    height: 12px;
    left: 334px;
    top: 690px;
  }
  .contact {
    position: absolute;
    top: 58px;
    left: 66px;
    writing-mode: vertical-rl;
    color: var(--ink-white);
    font-size: 19px;
    line-height: 1.2;
    letter-spacing: 0.08em;
    list-style: none;
    white-space: nowrap;
  }
  .contact__name {
    font-size: 22px;
    margin-left: 4px;
  }
  .contact__gap { margin-left: 16px; }
</style>
</head>
<body>
<main class="canvas">
  <section class="card card--front" aria-label="Card front">
    <div class="card__texture" role="img" aria-label="Dark carbon fibre weave texture"></div>
    <div class="brand brand--front">QUILLORB</div>
    <span class="brand-dot brand-dot--front"></span>
  </section>

  <section class="card card--back" aria-label="Card back">
    <div class="card__texture" role="img" aria-label="Dark carbon fibre weave texture"></div>
    <ul class="contact">
      <li class="contact__name">DORIAN ELWOOD MARSH</li>
      <li>EMAIL - DORIAN@QUILLORB.EXAMPLE</li>
      <li>MOBILE - 555 013 2867</li>
      <li class="contact__gap">WEB -</li>
      <li>QUILLORB.EXAMPLE: INVENTIVE TECHNOLOGY APPLICATIONS</li>
      <li>QUILLORB-TV.EXAMPLE: INNOVATIVE VIDEO ADVERTISING</li>
    </ul>
    <div class="brand brand--back">QUILLORB</div>
    <span class="brand-dot brand-dot--back"></span>
  </section>
</main>
</body>
</html>
```